Kelp Webcomic

A simple signup landing page and blog design for an upcoming webcomic. I am mostly looking for a flat UI with a simple color scheme. I want to showcase a large background image and the comic title image. I have all the technicals figured out (I am a web developer by trade), so all I need now is a solid design I like.

The signup for should only have one field (email) and have text above it, and smaller text below it.

The blog, I am thinking, should be in the style of comic book pages. The home page would be blocks with large white outlines, with the article pages being an extension of that. As I stated before, should be fairly minimalist, but fun. Also, no sidebar or ads, IE single column. I have attached a simple mockup/layout of the blog to give a general idea of what I am going for.

I have attached the Logo and Background art (uncolored) for reference. Don't worry about the background image blending in, I can take care of that when the design is implemented. I will be focusing on layout and overall look, not necessarily readability (which I can fix).

~Please DO NOT take these examples literally. I will describe what I like about each example.~

Signup pages:
http://example-plinth.com/landing-page-type-photo/
http://www.example-varnoq.com/showcase/website-design/814/10-most-beautiful-landing-pages-in-minimalist-style
http://example-quellbay.com/47-modern-landing-pages-showcasing-inspirational-web-design/
Great examples of minimalist design. However, instead of text or other content, there should be a simple signup form, as described above. Also think a lot more "playful" rather than super professional.

Blog:
http://example-vradd.no/
Awesome example of a single column, minimal design. Needs to be more "comicbook style" though.
http://example-tumbrik.com/
Another good example of minimal design blog.
http://example-morvane.net/wp-content/uploads/res-blogs-5.jpg
I like the timeline feel here. Combine that with a comic book page kind of thing, and I think you have a winner.

Actual webcomic landing (not required):
http://www.example-fennowhistle.com/comic.php?date=20021104#.U90ysYBdUvU
I like the navigation. It makes the atmosphere nice for the comic. The page layout itself is WAY too busy.
http://www.example-lodgeworth.com/comic/
Fairly common webcomic, but their navigation and page layout is nice.
http://example-qwib.com/936/
Another common webcomic. The simple page layout makes it easy for people to get started I think.

So there you have it. I will try my best to keep updating and adding to the description. If you have any questions, please don't hesitate to ask.

Hey Guys, I am really appreciating all the effort you have been putting in. I am amazed to see all the awesome designs and all the care taken with the project. I am just writing everyone to let you know that I have uploaded a simple layout/wireframe of the blog, to give an idea of what I am going for. Can't wait to see how things progress, and good luck to everyone!

Industry/Entity Type

Trade

Font styles to use
Sans Serif

Requirements
Must have
• Must showcase a large background image (does not have to cover the entire background). Should be a flat UI as well. Should be mostly neutral with splashes of blue or purple. Social links should also be somewhere (twitter, facebook, etc.).
Nice to have
• I am thinking something with rounded boxes, but I can live without them. A more "fun" design as opposed to more professional is definitely nice to have.

If you would like to try a stab at the actual comic page display and navigation, you are welcome to submit something. It should not be a main priority though.

Being responsive is not a requirement, but it would be nice to have.
Should not have
• A billion links in the navigation or look too busy.
No sidebar or advertisements. Should be a clean design.

```html
<!DOCTYPE html>
<html lang="en">
<head>
<meta charset="utf-8">
<title>Kelp Webcomic</title>
<link href="https://fonts.googleapis.com/css2?family=Open+Sans:wght@300;400;600&display=swap" rel="stylesheet">
<style>
:root{
  --sea:#41a5c4;
  --sea-deep:#1b5a6b;
  --footer:#1c5f71;
  --accent:#3aa6c8;
  --button:#22b8e6;
  --ink:#444;
  --muted:#777;
  --panel:#efefef;
  --line:#d8d8d8;
  --white:#fff;
  --plane:#d8dde3;
}
*{box-sizing:border-box;margin:0;padding:0}
html,body{width:832px;height:1200px;overflow:hidden}
body{font-family:"Open Sans",Arial,sans-serif;color:var(--ink);background:var(--white);position:relative}
.hero{position:absolute;left:0;top:0;width:832px;height:530px;
  background:radial-gradient(ellipse 330px 260px at 300px 260px,#11586a 0%,#2d8aa6 55%,var(--sea) 100%);
  border-bottom:2px solid #2a87a3}
.brand{position:absolute;left:34px;top:34px;font-size:50px;font-weight:300;color:#cfe3ea;letter-spacing:1px}
.hero-address{position:absolute;left:570px;top:43px;width:240px;font-size:10.3px;line-height:12.5px;color:var(--white)}
.intro{position:absolute;left:37px;top:155px;width:352px;color:var(--white)}
.intro-head{display:flex;align-items:center;gap:22px;padding-left:55px;height:32px;border-bottom:1px solid #7ec3d8;padding-bottom:6px;height:38px}
.intro-head h2{font-size:22px;font-weight:400}
.intro p{font-size:13.6px;line-height:25px;margin-top:12px;text-align:justify}
.intro p+p{margin-top:11px}
.signup{position:absolute;left:426px;top:160px;width:369px;height:327px;background:var(--panel);border:1px solid #cfcfcf}
.signup-head{background:var(--white);height:74px;border-bottom:1px solid var(--line);padding:12px 19px 0}
.signup-head h3{font-size:16px;font-weight:400;color:#333;display:flex;align-items:flex-end;gap:10px}
.signup-head p{font-size:11.5px;color:var(--muted);margin-top:7px}
.field{position:absolute;left:18px;width:333px;height:38px;background:var(--white);border:1px solid #ddd;border-radius:5px;font-size:11.5px;color:#999;padding:11px 14px}
.actions{position:absolute;left:18px;top:262px;display:flex;align-items:center;gap:10px}
.btn{display:flex;align-items:center;gap:6px;width:94px;height:32px;background:var(--button);border-radius:4px;color:var(--white);font-size:13px;padding-left:5px}
.legal{font-size:11.5px;color:#555}
.section-title{position:absolute;left:0;top:555px;width:832px;text-align:center;font-size:35px;font-weight:300;color:var(--accent)}
.rule{position:absolute;left:221px;top:603px}
.post-art{position:absolute;left:37px;top:675px;width:265px;height:262px;
  background:linear-gradient(135deg,#eef0f3 0%,var(--plane) 50%,#d41456 80%);border-radius:4px}
.post{position:absolute;left:414px;top:660px;width:381px}
.post h4{font-size:22px;font-weight:400;color:#444}
.meta{font-size:15px;color:#777;margin-top:16px;display:flex;align-items:center;gap:5px}
.post p{font-size:10.3px;line-height:17px;color:#444;text-align:justify;margin-top:12px}
.post p.first{margin-top:35px}
.post a{color:var(--accent);text-decoration:none}
.read-more{position:absolute;left:416px;top:882px}
.footer{position:absolute;left:0;top:979px;width:832px;height:221px;background:var(--footer);color:var(--white)}
.footer-brand{position:absolute;left:37px;top:22px;font-size:16px;color:#cfdfe5}
.footer-about{position:absolute;left:37px;top:61px;width:372px;font-size:9.8px;line-height:16.8px;text-align:justify}
.footer h5{font-size:17px;font-weight:400;position:absolute;top:19px}
.footer-contact{position:absolute;left:490px;top:58px;font-size:10.3px;line-height:16.8px}
.social{position:absolute;left:709px;top:54px;display:flex;gap:4px}
.social span{width:18px;height:18px;border-radius:3px;background:#2f8fb0;display:block}
.copyright{position:absolute;left:37px;top:186px;font-size:8.5px}
</style>
</head>
<body>
<header class="hero">
  <div class="brand">Kelp Webcomic</div>
  <address class="hero-address" style="font-style:normal">Address: Tidewater Row , 12b , Saltmarsh Allee , 10000 Brightwater<br>Country.<br>Telephone: +00 12 34567890<br>E-mail: hello@kelp-example.com</address>

  <section class="intro">
    <div class="intro-head">
      <svg width="18" height="20" viewBox="0 0 18 20"><path d="M1 1v19" stroke="#fff" stroke-width="1.6"/><path d="M1 2h16l-4 5 4 5H1z" fill="#fff"/></svg>
      <h2>Loremipsum</h2>
    </div>
    <p>Lorem Ipsum is simply dummy text of the printing and typesetting industry. Lorem ipsum dolor sit amet, consectetur adipiscing elit. Curabitur in mi vitae mi venenatis convallis. Nam porta dapibus volutpat.</p>
    <p>Lorem Ipsum is simply dummy text of the printing and typesetting industry. Lorem ipsum dolor sit amet, consectetur adipiscing elit. Curabitur in mi vitae mi venenatis convallis. Nam porta dapibus volutpat.</p>
  </section>

  <section class="signup">
    <div class="signup-head">
      <h3><svg width="26" height="26" viewBox="0 0 26 26"><path d="M3 23l2-6L19 3l4 4L9 21z" fill="none" stroke="#222" stroke-width="2"/><path d="M3 23l3-1" stroke="#222" stroke-width="2"/></svg>Get in touch</h3>
      <p>Please complete the form and we will get back to you.</p>
    </div>
    <div class="field" style="top:93px">Name</div>
    <div class="field" style="top:143px">Email</div>
    <div class="field" style="top:193px;height:54px">Message</div>
    <div class="actions">
      <div class="btn"><svg width="24" height="22" viewBox="0 0 24 22"><circle cx="10" cy="12" r="9" fill="none" stroke="#fff" stroke-width="1.6"/><path d="M5 12l4 4 13-14" fill="none" stroke="#fff" stroke-width="2.4"/></svg>Sign Up!</div>
      <span class="legal">Privacy Policy | Terms &amp; Conditions</span>
    </div>
  </section>
</header>

<h2 class="section-title">Latest post</h2>
<svg class="rule" width="390" height="18" viewBox="0 0 390 18"><path d="M0 9h180M210 9h180" stroke="#62b4cf" stroke-width="1"/><path d="M195 1l2.5 5 5.5-1-3 4.5 3 4.5-5.5-1-2.5 5-2.5-5-5.5 1 3-4.5-3-4.5 5.5 1z" fill="#3aa6c8"/></svg>

<div class="post-art" role="img" aria-label="Illustration of a white and pink folded paper plane"></div>
<article class="post">
  <h4>Lorem Ipsum is simply dummy</h4>
  <div class="meta">
    <svg width="10" height="10"><rect x=".5" y="1.5" width="9" height="8" fill="none" stroke="#bbb"/></svg>23 may 2014,
    <svg width="10" height="10"><circle cx="5" cy="3" r="2.5" fill="#bbb"/><path d="M0 10q5-6 10 0z" fill="#bbb"/></svg>admin,
    <svg width="14" height="10"><ellipse cx="7" cy="4.5" rx="6.5" ry="4" fill="#bbb"/></svg>15,
    <svg width="16" height="11"><path d="M8 10L2 4a2.5 2.5 0 0 1 6-3 2.5 2.5 0 0 1 6 3z" fill="#bbb"/></svg>7
  </div>
  <p class="first">It is a long established fact that a reader will be distracted by the readable content of a page when looking at its layout.</p>
  <p>It was popularised in the <a href="#">1960s with the release</a> of Stenmark sheets containing Lorem Ipsum passages, and more recently with desktop publishing software like Quillset Layout including versions of Lorem Ipsum.</p>
</article>
<svg class="read-more" width="90" height="34" viewBox="0 0 90 34"><path d="M0 0h73l15 16-15 16H0z" fill="#a9a9a9"/><path d="M0 0h72l14 15-14 15H0z" fill="#c6c6c6"/><text x="18" y="20" font-family="Open Sans, sans-serif" font-size="10.3" fill="#444">Read more</text></svg>

<footer class="footer">
  <div class="footer-brand">Kelp Webcomic</div>
  <p class="footer-about">Lorem Ipsum is simply dummy text of the printing and typesetting industry. Lorem Ipsum has been the industry's standard dummy text ever since the 1500s, when an unknown printer into electronic typesetting,remaining essentially unchanged.orem Ipsum is simply dummy text of the printing and typesettustry.</p>
  <h5 style="left:490px">Contact Us</h5>
  <address class="footer-contact" style="font-style:normal">Address: Tidewater Row , 12b<br>Saltmarsh Allee , 12b<br>10000 Brightwater<br>Northland<br>Telephone: +00 12 34567890<br>E-mail: hello@kelp-example.com</address>
  <h5 style="left:709px">Follow Us</h5>
  <div class="social" aria-label="Social links"><span></span><span></span><span></span><span></span></div>
  <div class="copyright">Copyrights© 2014 , Kelp Webcomic</div>
</footer>
</body>
</html>
```